Great Opportunity !! Masters in Business Analytics College Course

the size is Full Page, with bleed*
8”x 10.75" plus 0.25" bleed.
please leave one inch for footer
the purpose is attract students to join this college program .
this is for students in USA .
college age of around 24 years old
I am looking for a flyer that is unique and shows creativity .
A flyer that people would want to look at it because it is unique.
you can choose either vector, text ,or picture.
if you do picture it should be a white USA citizen wearing a white solid shirt and not long hair

Target Market(s)

USA students about 23 in age to join this college program

Industry/Entity Type

education

Colors
0054AA
0677BA
7BADD7
CADEEF
E8F1F8
0094D4
00A9DD
6FCCEA
C7EBF8
E9F6FB

Requirements
Must have
• the text should not be crowded .. .. .. the ad should not be full of text
Should not have
• not have very large text .. it should not be a flyer that is full of text .. you have to figure out how to avoid looking at the ad and it is very busy with text

```html
<!DOCTYPE html>
<html lang="en">
<head>
<meta charset="utf-8">
<title>Master's in Business Analytics – Open House Flyer</title>
<link rel="stylesheet" href="https://fonts.googleapis.com/css2?family=Poppins:wght@500;600;700;800&family=Oswald:wght@500;600&display=swap">
<style>
  :root{
    --page:#ffffff;
    --navy:#0b2a66;
    --navy-deep:#14203d;
    --spot:#3a4154;
    --yellow:#ffe21a;
    --white:#ffffff;
    --sky:#6cc8f3;
    --sky-dark:#2f8fd6;
    --red:#e0241b;
    --ink:#0d2b66;
    --pill:#10172a;
  }
  *{box-sizing:border-box;margin:0;padding:0}
  html,body{width:1200px;height:2701px;overflow:hidden;background:var(--page)}
  body{position:relative;font-family:'Poppins',sans-serif}
  .flyer{
    position:absolute;left:71px;top:666px;width:1058px;height:1368px;
    box-shadow:0 6px 22px rgba(0,0,0,.35);
    background:var(--page);overflow:hidden;
  }
  .flyer-art{
    position:absolute;left:0;top:0;width:1058px;height:1245px;
    background:linear-gradient(180deg,#0b3270 0%,#0d2758 35%,var(--navy-deep) 100%);
  }
  .spotlight{position:absolute;left:0;top:0}
  .footer{position:absolute;left:0;top:1245px;width:1058px;height:123px;background:var(--page)}
  .abs{position:absolute}
  .center{left:0;width:1058px;text-align:center}
  .headline{top:88px;font-weight:800;font-size:46px;line-height:48px;letter-spacing:.3px}
  .headline .yellow{color:var(--yellow)}
  .headline .white{color:var(--white)}
  .rule{position:absolute;height:2px;background:rgba(120,150,200,.35)}
  .program{top:250px;font-weight:800;font-size:34px;line-height:38px;color:var(--yellow)}
  .tagline{top:328px;font-weight:500;font-size:29px;color:var(--white)}
  .banner-tail{position:absolute;left:340px;top:420px}
  .banner{
    position:absolute;left:172px;top:400px;width:720px;height:90px;background:var(--sky);
    clip-path:polygon(0 0,96% 0,100% 100%,2% 100%);text-align:center;padding-top:6px;
  }
  .banner-title{font-family:'Oswald',sans-serif;font-weight:600;font-size:42px;line-height:46px;color:var(--ink);letter-spacing:-.5px}
  .banner-title .amount{color:var(--red)}
  .banner-title sup{font-size:22px}
  .banner-note{font-weight:500;font-size:23px;line-height:28px;color:var(--ink)}
  .megaphone{position:absolute;left:112px;top:470px;width:110px;height:80px;border-radius:40px;
    background:linear-gradient(135deg,#e9ecf1,#b9c0cb)}
  .roles{position:absolute;left:175px;top:564px;list-style:none}
  .roles li{font-weight:600;font-size:24px;line-height:40px;color:var(--white);padding-left:28px;width:232px;white-space:nowrap}
  .roles li.shade{background:linear-gradient(90deg,rgba(30,60,120,.55),rgba(30,60,120,0))}
  .hired{position:absolute;left:457px;top:556px}
  .hired h2{font-weight:700;font-size:33px;color:var(--sky);line-height:42px;white-space:nowrap}
  .employers{list-style:none;display:grid;grid-template-columns:170px 250px;margin-top:4px}
  .employers li{font-weight:600;font-size:25px;line-height:35px;color:var(--white);display:flex;align-items:center;gap:12px;white-space:nowrap}
  .tick{flex:none;width:15px;height:15px;border-radius:50%;background:var(--yellow);display:inline-flex;align-items:center;justify-content:center}
  .open-tag{position:absolute;left:412px;top:747px;width:236px;height:34px;background:var(--sky);
    clip-path:polygon(6% 0,100% 0,94% 100%,0 100%);text-align:center;font-weight:700;font-size:28px;line-height:34px;color:var(--ink)}
  .event{position:absolute;left:0;width:1058px;top:790px;display:flex;justify-content:center;align-items:center;gap:14px;font-weight:700;font-size:32px;color:var(--white)}
  .event .date{background:var(--red);padding:0 12px;line-height:44px;border-radius:4px}
  .contact{position:absolute;left:309px;top:855px;width:440px;height:32px;background:var(--pill);border-radius:6px;
    display:flex;align-items:center;justify-content:center;gap:8px;font-size:19px;font-weight:600;color:var(--white);white-space:nowrap}
  .contact .hl{color:var(--yellow)}
  .college{top:905px;font-weight:600;font-size:31px;color:var(--sky)}
  .accred{position:absolute;left:280px;top:952px;display:flex;align-items:center;gap:14px}
  .accred .stat{font-family:'Oswald',sans-serif;font-weight:600;font-size:44px;color:var(--yellow);line-height:48px;white-space:nowrap}
  .accred p{font-weight:600;font-size:20px;line-height:23px;color:var(--white);white-space:nowrap}
  .celebration{position:absolute;left:270px;top:1010px;width:520px;height:235px;
    background:linear-gradient(180deg,rgba(120,124,132,.0) 0%,rgba(110,115,124,.55) 45%,#2b2f38 100%)}
</style>
</head>
<body>
  <main class="flyer">
    <section class="flyer-art">
      <svg class="spotlight" width="1058" height="1245" viewBox="0 0 1058 1245" aria-hidden="true">
        <defs>
          <linearGradient id="beam" x1="0" y1="0" x2="0" y2="1">
            <stop offset="0" stop-color="#0d2f6c" stop-opacity="0.4"/>
            <stop offset="1" stop-color="#3a4154"/>
          </linearGradient>
        </defs>
        <polygon points="45,200 1013,200 820,1245 238,1245" fill="url(#beam)"/>
      </svg>

      <h1 class="abs center headline"><span class="yellow">DO YOU HAVE AN ANALYTICAL MIND</span><br><span class="white">AND SEEKING A PROFITABLE CAREER?</span></h1>
      <div class="rule" style="left:100px;top:218px;width:858px"></div>

      <h2 class="abs center program">A MASTER'S IN BUSINESS ANALYTICS-HARLOW<br>STATE COLLEGE**</h2>
      <p class="abs center tagline">Can prepare you for some of the most in-demand jobs.</p>

      <svg class="banner-tail" width="90" height="96" viewBox="0 0 90 96" aria-hidden="true">
        <polygon points="0,60 90,60 80,96 0,90" fill="var(--sky-dark)"/>
      </svg>
      <div class="banner">
        <div class="banner-title">JOBS WITH A MEDIAN SALARY OF <span class="amount"><sup>$</sup>100K+</span></div>
        <div class="banner-note">(NATIONAL CAREERS SURVEY 2023)</div>
      </div>
      <div class="megaphone" role="img" aria-label="Megaphone illustration"></div>

      <ul class="roles">
        <li>BI Developer</li>
        <li class="shade">Data Analyst</li>
        <li>Data Scientist</li>
        <li class="shade">Data Developer</li>
      </ul>

      <div class="hired">
        <h2>Graduates were hired at:</h2>
        <ul class="employers">
          <li><span class="tick"><svg width="9" height="9" viewBox="0 0 10 10"><path d="M1.5 5.2 4 7.5 8.5 2.5" fill="none" stroke="#1a2340" stroke-width="2"/></svg></span>Norvale</li>
          <li><span class="tick"><svg width="9" height="9" viewBox="0 0 10 10"><path d="M1.5 5.2 4 7.5 8.5 2.5" fill="none" stroke="#1a2340" stroke-width="2"/></svg></span>Brightmoor</li>
          <li><span class="tick"><svg width="9" height="9" viewBox="0 0 10 10"><path d="M1.5 5.2 4 7.5 8.5 2.5" fill="none" stroke="#1a2340" stroke-width="2"/></svg></span>Voltrane</li>
          <li><span class="tick"><svg width="9" height="9" viewBox="0 0 10 10"><path d="M1.5 5.2 4 7.5 8.5 2.5" fill="none" stroke="#1a2340" stroke-width="2"/></svg></span>Keystone Mutual</li>
          <li><span class="tick"><svg width="9" height="9" viewBox="0 0 10 10"><path d="M1.5 5.2 4 7.5 8.5 2.5" fill="none" stroke="#1a2340" stroke-width="2"/></svg></span>Coretex</li>
        </ul>
      </div>

      <div class="rule" style="left:200px;top:734px;width:670px"></div>

      <div class="open-tag">OPEN HOUSE</div>
      <div class="event"><span>WEDNESDAY</span><span class="date">APRIL 20</span><span>7:30 PM</span></div>
      <div class="contact">
        <span class="hl">Email</span>
        <svg width="14" height="12" viewBox="0 0 14 12" aria-hidden="true"><rect x="1" y="1" width="12" height="10" rx="1.5" fill="none" stroke="#6cc8f3" stroke-width="1.6"/><path d="M1.5 2 7 6.5 12.5 2" fill="none" stroke="#6cc8f3" stroke-width="1.6"/></svg>
        <span>alexreed@mailbox.com</span>
        <span class="hl">for the link!</span>
      </div>

      <p class="abs center college">** Harlow State College</p>
      <div class="accred">
        <span class="stat">ONLY 5%</span>
        <p>of universities achieve prestigious<br>IBEA accreditation.</p>
      </div>

      <div class="celebration" role="img" aria-label="Silhouettes of graduates tossing caps in the air"></div>
    </section>
    <footer class="footer"></footer>
  </main>
</body>
</html>
```